Marlow Crest Group (Real Estate and Investment)

A high end, clean design.
We are a real estate company with sales, asset management and investment divisions. We want to use a black and white scheme which is really high end feel. The back of the card can just be the logo (black background with the white writing) as we will probably emboss this when we print)

Target Market(s)

High level investors, high end houses for sale

Industry/Entity Type

Business

Contact Information for Business Card

Name, position, phone number and email address
Glen Varley, Managing Director, 0437259064 and glen@marlowcrest-example.com.au

Requirements
Must have
• Back of the card to be the black background with the white writing (as per the attached images). Would like the capacity to emboss the writing and logo

```html
<!DOCTYPE html>
<html lang="en">
<head>
<meta charset="utf-8">
<title>Marlow Crest Group – Business Card</title>
<link rel="stylesheet" href="https://fonts.googleapis.com/css2?family=Inter:wght@400&family=Open+Sans:wght@400&family=Tinos&display=swap">
<style>
  :root {
    --stage: #8e8e8e;
    --ink: #000000;
    --paper: #ffffff;
    --text: #454545;
    --shadow: rgba(0, 0, 0, 0.35);
  }
  * { margin: 0; padding: 0; box-sizing: border-box; }
  html, body {
    width: 980px;
    height: 1200px;
    overflow: hidden;
    background: var(--stage);
  }
  .canvas { position: relative; width: 980px; height: 1200px; }

  .card {
    position: absolute;
    overflow: hidden;
    box-shadow: 0 14px 14px -10px var(--shadow);
  }
  .card--front {
    left: 117px; top: 130px; width: 725px; height: 410px;
    background: var(--ink);
  }
  .card--back {
    left: 117px; top: 709px; width: 718px; height: 413px;
    background: var(--paper);
  }
  .card__art { position: absolute; inset: 0; }

  .brand-name {
    position: absolute;
    left: 0; right: 0;
    text-align: center;
    color: var(--paper);
    font-family: "Inter", sans-serif;
    font-weight: 400;
    letter-spacing: -0.5px;
    white-space: nowrap;
  }
  .card--front .brand-name { top: 282px; font-size: 34px; }
  .card--back .brand-name { top: 247px; width: 300px; font-size: 21px; }

  .contact {
    position: absolute;
    color: var(--text);
    white-space: nowrap;
    font-family: "Open Sans", sans-serif;
  }
  .contact__name { left: 403px; top: 47px; font-size: 29px; }
  .contact__role { left: 385px; top: 91px; font-size: 20px; }
  .contact__phone { left: 387px; top: 179px; font-size: 26px; font-family: "Tinos", serif; }
  .contact__email { left: 383px; top: 248px; font-size: 19.5px; }
</style>
</head>
<body>
<main class="canvas">

  <section class="card card--front" aria-label="Card front">
    <svg class="card__art" width="725" height="410" viewBox="0 0 725 410" aria-hidden="true">
      <circle class="brand-mark" cx="362" cy="166" r="81" fill="none" stroke="#fff" stroke-width="2.5"/>
    </svg>
    <p class="brand-name">MARLOW CREST GROUP</p>
  </section>

  <section class="card card--back" aria-label="Card back">
    <svg class="card__art" width="718" height="413" viewBox="0 0 718 413" aria-hidden="true">
      <polygon class="brand-panel" points="0,0 229,0 309,80 309,328 229,413 0,413" fill="#000"/>
      <circle class="brand-mark" cx="150" cy="173" r="53" fill="none" stroke="#fff" stroke-width="2"/>

      <!-- person badge -->
      <polygon points="330,60 358,60 373,85 358,110 330,110 315,85" fill="#000"/>
      <circle cx="344" cy="85" r="16" fill="#fff"/>
      <circle cx="344" cy="80" r="5" fill="#000"/>
      <path d="M335 94 a9 8 0 0 1 18 0 z" fill="#000"/>

      <!-- contact strip -->
      <polygon points="318,141 362,141 373,215 364,323 323,323 313,215" fill="#000"/>

      <!-- phone icon -->
      <path d="M335 180 c2 -2 5 -2 6 1 l3 6 c1 2 0 4 -2 5 l-2 1 c2 5 6 9 11 11 l1 -2 c1 -2 3 -3 5 -2 l6 3 c3 1 3 4 1 6 l-3 3 c-3 3 -8 3 -13 0 c-7 -4 -13 -10 -16 -17 c-2 -5 -2 -9 0 -12 z" fill="#fff"/>

      <!-- envelope icon -->
      <rect x="330" y="252" width="30" height="22" fill="#fff"/>
      <path d="M331 253 l14 12 l14 -12" fill="none" stroke="#000" stroke-width="1.6"/>
      <path d="M331 273 l10 -9 M359 273 l-10 -9" stroke="#000" stroke-width="1.4"/>
      <circle cx="345" cy="249" r="7" fill="#fff" stroke="#000" stroke-width="1.2"/>
      <text x="345" y="252.5" font-size="9" text-anchor="middle" font-family="Open Sans, sans-serif" fill="#000">@</text>
    </svg>

    <p class="brand-name">MARLOW CREST GROUP</p>

    <p class="contact contact__name">Glen Varley</p>
    <p class="contact contact__role">Managing Director</p>
    <p class="contact contact__phone">0437259064</p>
    <p class="contact contact__email">glen@marlowcrest-example.com.au</p>
  </section>

</main>
</body>
</html>
```